stationary for hygienic company

We need a stationary design for hygienic company which provides public high end sanitary products and high end public lavatory.
We need a fresh and clean style stationary
we want the following things:
* logo (redesigned in eps/vector)
* Letterhead (with company details)
* letterhead (without company details)
* Business card
* note block
* ballpoint
* etcetera (a complete package)

```html
<!DOCTYPE html>
<html lang="fr">
<head>
<meta charset="utf-8">
<title>Velmora – Presentation Folder</title>
<link href="https://fonts.googleapis.com/css2?family=Questrial&family=Open+Sans:wght@400;600&display=swap" rel="stylesheet">
<style>
  :root {
    --backdrop: #e6e6e6;
    --paper: #ffffff;
    --cover-grey: #b9b9b9;
    --ink: #1f1f1f;
    --ink-soft: #4a4a4a;
    --brand-magenta: #d4177f;
    --brand-cyan: #2aa3d8;
    --brand-navy: #2d2a6e;
  }
  * { margin: 0; padding: 0; box-sizing: border-box; }
  html, body { width: 1200px; height: 847px; overflow: hidden; }
  body {
    background: var(--backdrop);
    font-family: "Questrial", "Open Sans", sans-serif;
    color: var(--ink);
    position: relative;
  }
  .folder-panel {
    position: absolute;
    background: var(--paper);
    box-shadow: 0 6px 18px rgba(0,0,0,0.12);
    display: flex;
    flex-direction: column;
    align-items: center;
    overflow: hidden;
  }
  .folder-cover {
    left: 105px; top: 125px; width: 290px; height: 560px;
    background: linear-gradient(180deg, #c9c9c9, var(--cover-grey));
  }
  .folder-inside-left  { left: 550px; top: 155px; width: 272px; height: 500px; }
  .folder-inside-right { left: 824px; top: 155px; width: 272px; height: 500px; }

  .brand-block {
    display: flex; flex-direction: column; align-items: center;
    margin-top: 105px;
  }
  .folder-cover .brand-block { margin-top: 110px; }
  .brand-dot {
    width: 46px; height: 46px; border-radius: 50%;
    background: var(--brand-magenta);
    margin-bottom: 22px;
  }
  .brand-name {
    font-size: 56px; line-height: 1; letter-spacing: 0.5px;
    color: var(--ink);
  }
  .brand-tagline {
    font-size: 19px; color: var(--ink-soft); margin-top: 8px; letter-spacing: 0.5px;
  }
  .brand-legal {
    font-family: "Open Sans", sans-serif;
    font-size: 8px; color: var(--ink-soft); margin-top: 12px;
  }
  .cover-web {
    position: absolute; bottom: 40px; left: 0; right: 0; text-align: center;
    font-family: "Open Sans", sans-serif; font-size: 17px; color: var(--brand-navy);
  }
  .pocket {
    position: absolute; left: 0; right: 0; bottom: 0; height: 155px;
    border-radius: 8px 8px 0 0;
  }
  .pocket-magenta { background: var(--brand-magenta); }
  .pocket-cyan    { background: var(--brand-cyan); }
</style>
</head>
<body>
  <section class="folder-panel folder-cover">
    <div class="brand-block">
      <span class="brand-dot"></span>
      <h1 class="brand-name">Velmora</h1>
      <p class="brand-tagline">Boutique Hygienique</p>
      <p class="brand-legal">Marque déposée</p>
    </div>
    <p class="cover-web">www.velmora-hygiene.com</p>
  </section>

  <section class="folder-panel folder-inside-left">
    <div class="brand-block">
      <span class="brand-dot"></span>
      <h2 class="brand-name">Velmora</h2>
      <p class="brand-tagline">Boutique Hygienique</p>
      <p class="brand-legal">Marque déposée</p>
    </div>
    <div class="pocket pocket-magenta"></div>
  </section>

  <section class="folder-panel folder-inside-right">
    <div class="brand-block">
      <span class="brand-dot"></span>
      <h2 class="brand-name">Velmora</h2>
      <p class="brand-tagline">Boutique Hygienique</p>
      <p class="brand-legal">Marque déposée</p>
    </div>
    <div class="pocket pocket-cyan"></div>
  </section>
</body>
</html>
```